BRANDHILL real estate family office

Hello, Our business is a real estate intermediation activity on high-end goods (amounts exceeding € 10m) for corporate and private clients. You can see our logo on the site www.brandhill-demo.fr We would like to keep that spirit with the hexagon that represents France (transactions between Monaco and Saint Tropez, Courchevel and Paris). And the "baseline" that is "real estate family office". The corporate logo should be and can be printed by embossing (relief). We must integrate the name, first name, phone, email and website. Finally, to imbibe the spirit of business, here is a detail of the activity. "Genuine consulting firm in real estate investments, BRANDHILL works with its customers as a specialized player in the high-end markets, we are recognized for our ultra-confidential approach and tailor-made, as well as the quality of our network. We broadcast any information on the market and we work exclusively through a strong relationship we have developed over the years. BRANDHILL is active on the French Riviera (from Monaco to Saint-Tropez), the Alps (Courchevel, Méribel, Megève) and Paris (essentially market premium). Always looking for opportunities for our clients, we work on two investment areas: residential luxury real estate (properties, vineyards, mansions, land, etc.) commercial real estate (empty office buildings or yield, hotel properties, land, etc.) "

Target Market(s)

High foreign end customers. corporate and private.

Industry/Entity Type

Real Estate

Contact Information for Business Card

LOGO
baseline
Laurent Dufossé
+33(0)6.41.57.09.64
ld@brandhill-demo.fr
www.brandhill-demo.fr

Font styles to use
Serif

Colors
cedeed
0255a3
3277b5
85abd2
85cae6
34a7d7
0792cd
cfdeed
1b1b1b

Requirements
Must have
• see description

```html
<!DOCTYPE html>
<html lang="fr">
<head>
<meta charset="utf-8">
<title>BRANDHILL – business card</title>
<link rel="stylesheet" href="https://fonts.googleapis.com/css2?family=Josefin+Sans:wght@300;400;600&family=Libre+Baskerville:wght@400&display=swap">
<style>
  :root {
    --canvas: #2b2b2b;
    --card: #050505;
    --white: #ffffff;
    --blue: #2d47a6;
    --rule: #bdbdbd;
  }
  * { box-sizing: border-box; margin: 0; padding: 0; }
  html, body {
    width: 1200px;
    height: 900px;
    overflow: hidden;
    background: var(--canvas);
  }
  .canvas {
    width: 1200px;
    height: 900px;
    display: flex;
    flex-direction: column;
    align-items: center;
    justify-content: center;
    gap: 40px;
  }
  .card {
    width: 700px;
    height: 390px;
    background: var(--card);
    border-radius: 26px;
    position: relative;
    overflow: hidden;
  }

  /* Front */
  .card--front {
    display: flex;
    flex-direction: column;
    align-items: center;
    justify-content: center;
  }
  .wordmark {
    font-family: "Josefin Sans", sans-serif;
    font-weight: 300;
    font-size: 78px;
    letter-spacing: 6px;
    color: var(--white);
    line-height: 1;
  }
  .baseline {
    font-family: "Josefin Sans", sans-serif;
    font-weight: 300;
    font-size: 24px;
    letter-spacing: 3px;
    color: var(--blue);
    margin-top: 6px;
    align-self: center;
    padding-left: 170px;
  }
  .front-url {
    font-family: "Josefin Sans", sans-serif;
    font-weight: 400;
    font-size: 22px;
    letter-spacing: 1px;
    color: var(--white);
    margin-top: 62px;
  }
  .front-url .domain { color: var(--blue); font-weight: 600; }

  /* Back */
  .card--back {
    display: flex;
    align-items: center;
  }
  .brand-block {
    width: 330px;
    display: flex;
    flex-direction: column;
    align-items: center;
    gap: 18px;
    padding-top: 60px;
  }
  .brand-block .square {
    width: 34px;
    height: 34px;
    background: var(--blue);
  }
  .brand-block .brand-name {
    font-family: "Josefin Sans", sans-serif;
    font-weight: 300;
    font-size: 40px;
    letter-spacing: 4px;
    color: var(--white);
  }
  .divider {
    width: 1px;
    height: 130px;
    background: linear-gradient(to bottom, transparent, var(--rule), transparent);
    margin-top: 10px;
  }
  .contact {
    padding-left: 38px;
    padding-bottom: 30px;
  }
  .person-name {
    font-family: "Libre Baskerville", serif;
    font-size: 25px;
    letter-spacing: 1px;
    text-transform: uppercase;
    color: var(--blue);
    margin-bottom: 14px;
  }
  .contact-list { list-style: none; }
  .contact-list li {
    display: flex;
    align-items: center;
    gap: 12px;
    font-family: "Josefin Sans", sans-serif;
    font-size: 19px;
    color: var(--white);
    line-height: 1.45;
  }
  .contact-list svg { width: 14px; height: 14px; flex: none; }
  .contact-list .domain { color: var(--blue); }
</style>
</head>
<body>
<main class="canvas">

  <section class="card card--front">
    <div class="wordmark">BRANDHILL</div>
    <div class="baseline">real estate family office</div>
    <div class="front-url">www.<span class="domain">brandhill-demo</span>.fr</div>
  </section>

  <section class="card card--back">
    <div class="brand-block">
      <span class="square"></span>
      <span class="brand-name">BRANDHILL</span>
    </div>
    <div class="divider"></div>
    <div class="contact">
      <h1 class="person-name">Laurent Dufossé</h1>
      <ul class="contact-list">
        <li>
          <svg viewBox="0 0 24 24" aria-hidden="true"><path fill="#2d47a6" d="M6.6 10.8a15.1 15.1 0 0 0 6.6 6.6l2.2-2.2a1 1 0 0 1 1-.25 11.4 11.4 0 0 0 3.6.57 1 1 0 0 1 1 1V20a1 1 0 0 1-1 1A17 17 0 0 1 3 4a1 1 0 0 1 1-1h3.5a1 1 0 0 1 1 1c0 1.25.2 2.45.57 3.57a1 1 0 0 1-.25 1z"/></svg>
          +33(0)6.41.57.09.64
        </li>
        <li>
          <svg viewBox="0 0 24 24" aria-hidden="true"><rect x="2.5" y="5" width="19" height="14" rx="1.5" fill="none" stroke="#2d47a6" stroke-width="2"/><path d="M3 6l9 7 9-7" fill="none" stroke="#2d47a6" stroke-width="2"/></svg>
          ld@brandhill-demo.fr
        </li>
        <li>
          <svg viewBox="0 0 24 24" aria-hidden="true"><circle cx="12" cy="12" r="9.5" fill="none" stroke="#2d47a6" stroke-width="2"/><path d="M2.5 12h19M12 2.5c3 3 3 16 0 19M12 2.5c-3 3-3 16 0 19" fill="none" stroke="#2d47a6" stroke-width="1.6"/></svg>
          <span>www.<span class="domain">brandhill-demo</span>.fr</span>
        </li>
      </ul>
    </div>
  </section>

</main>
</body>
</html>
```